Website design for a high-end equestrian business

Design a website to replace current one. Clean, simple, elegant design. I run a business training show jumping riders and horses, as well as buying and selling high quality horses. I run my business from a beautiful yard in Co. Kildare, Ireland. Reference to Ireland and quality sport horses is important in the website.

Current website is www.helenacarrowmere.com. One page in particular that I need is a "Sport Horses" page as well as a "References" page. Layout for each to be similar to this one - https://www.brayleymeadow.net/en/sporthorses

Another website I like the feel of is www.veltrahunters.com
Colour theme to be charcoal grey with elements of lighter grey and cream, as per logo. Charcoal grey to be somewhat transparent, otherwise it takes over too much. Cream colour is also to be subtle and not too beige.

Please note that Carrowmere is one word.

Please note there are new photographs with which to work if desired.
Updates

Sick

Target Market(s)

Upmarket clients seeking high quality coaching services and high quality show jumping horses

Number of Pages Required

2 page

Font styles to use
Serif
Sans Serif

Colors

Designer to choose only greyscale colors for use in the design.

Requirements
Must have
• A clean, simple, elegant look to the final design. OVerall theme colours must be subtle and include charcoal grey, light grey and cream. A design that will work well for mobile also. Please include only photographs provided or on the old website.
Nice to have
• artistically integrated photographs. use of the logo.
Should not have
• Anything fussy.

```html
<!DOCTYPE html>
<html lang="en">
<head>
<meta charset="utf-8">
<title>Helena Carrowmere — Show Jumping</title>
<link rel="stylesheet" href="https://fonts.googleapis.com/css2?family=EB+Garamond:wght@400;500&family=Open+Sans:wght@400;600&display=swap">
<style>
  :root {
    --charcoal: #0c0c0c;
    --charcoal-soft: #1a1a1a;
    --gold: #c3a968;
    --white: #ffffff;
    --ink: #222222;
    --muted: #5a5a5a;
    --page-bg: #e9e9e9;
  }
  * { margin: 0; padding: 0; box-sizing: border-box; }
  html, body { width: 1200px; height: 864px; overflow: hidden; background: var(--page-bg); }
  body { font-family: "Open Sans", Arial, sans-serif; color: var(--ink); }

  .site { width: 1200px; height: 864px; position: relative; overflow: hidden; background: var(--white); }

  .site-header {
    height: 84px; background: var(--charcoal);
    display: flex; align-items: center; justify-content: space-between;
    padding: 0 150px 0 150px;
  }
  .brand { font-family: "EB Garamond", Georgia, serif; font-size: 24px; color: var(--gold); font-weight: 400; letter-spacing: .5px; }
  .main-nav { display: flex; gap: 22px; list-style: none; }
  .main-nav li { font-family: "EB Garamond", Georgia, serif; font-size: 13px; color: var(--white); }
  .main-nav .has-sub::after { content: " \25BE"; font-size: 9px; }

  .hero { position: relative; height: 460px; overflow: hidden; }
  .hero-photo {
    position: absolute; inset: 0;
    background: linear-gradient(180deg, #4d5a3e 0%, #3f5233 45%, #5b4a36 80%, #3b2e22 100%);
  }
  .hero-overlay { position: absolute; inset: 0; background: rgba(20,20,20,.45); }
  .hero-content { position: absolute; inset: 0; text-align: center; color: var(--white); padding-top: 92px; }
  .hero-title { font-family: "EB Garamond", Georgia, serif; font-weight: 400; font-size: 44px; }
  .hero-sub { font-family: "EB Garamond", Georgia, serif; color: var(--gold); font-size: 20px; margin-top: 14px; }
  .hero-text { font-size: 13px; line-height: 1.55; width: 480px; margin: 16px auto 0; }
  .btn-gold {
    display: inline-block; background: var(--gold); color: var(--white);
    font-family: "EB Garamond", Georgia, serif; font-size: 14px; letter-spacing: .5px;
    padding: 6px 28px; margin-top: 24px;
  }
  .slider-arrow { position: absolute; top: 212px; width: 44px; height: 44px; }
  .slider-arrow.prev { left: 50px; }
  .slider-arrow.next { right: 50px; }

  .welcome { height: 220px; display: flex; position: relative; }
  .welcome-text { width: 560px; padding: 28px 0 0 150px; }
  .section-title { font-family: "EB Garamond", Georgia, serif; font-size: 24px; font-weight: 400; color: var(--ink); }
  .section-title .accent { color: var(--gold); }
  .welcome-body { font-size: 11px; line-height: 1.6; color: var(--muted); margin-top: 12px; width: 400px; }
  .btn-small { font-size: 11px; padding: 4px 16px; margin-top: 12px; }
  .welcome-photo {
    flex: 1; background: linear-gradient(90deg, #ffffff 0%, #c9b8a6 30%, #7a5236 60%, #4b3222 100%);
  }

  .services { height: 100px; background: var(--charcoal-soft); text-align: center; padding-top: 18px; }
  .services .section-title { color: var(--gold); font-size: 22px; }
  .dots { color: var(--gold); font-size: 10px; letter-spacing: 3px; margin-top: 2px; }
  .services-text { color: #9a9a9a; font-size: 11px; margin-top: 6px; }
</style>
</head>
<body>
<div class="site">
  <header class="site-header">
    <div class="brand">Helena Carrowmere</div>
    <ul class="main-nav">
      <li>Home</li><li>About</li><li class="has-sub">Horses</li><li>Sponsors</li>
      <li class="has-sub">Facilities &amp; Services</li><li>Gallery</li><li>Contact</li>
    </ul>
  </header>

  <section class="hero">
    <div class="hero-photo" role="img" aria-label="Rider in a helmet on a bay horse among green trees"></div>
    <div class="hero-overlay"></div>
    <div class="hero-content">
      <h1 class="hero-title">Discover the Beauty</h1>
      <p class="hero-sub">of horse riding</p>
      <p class="hero-text">Lorem Ipsum is simply dummy text of the printing and typesetting industry. Lorem Ipsum has been the industry's standard dummy text ever since the 1500s.</p>
      <span class="btn-gold">READ MORE</span>
    </div>
    <svg class="slider-arrow prev" viewBox="0 0 44 44" aria-hidden="true">
      <circle cx="22" cy="22" r="22" fill="rgba(0,0,0,.55)"/>
      <path d="M25 14 L17 22 L25 30" fill="none" stroke="#fff" stroke-width="1.8"/>
    </svg>
    <svg class="slider-arrow next" viewBox="0 0 44 44" aria-hidden="true">
      <circle cx="22" cy="22" r="22" fill="rgba(0,0,0,.55)"/>
      <path d="M19 14 L27 22 L19 30" fill="none" stroke="#fff" stroke-width="1.8"/>
    </svg>
  </section>

  <section class="welcome">
    <div class="welcome-text">
      <h2 class="section-title">Welcome To <span class="accent">Helena Carrowmere</span></h2>
      <p class="welcome-body">Helena is an accomplished rider, sport horse producer and equestrian coach. Working from a quiet yard in County Kildare, she has brought many young horses through the grades and guided riders to success at national and international shows. Her calm, patient approach builds confidence in horse and rider alike, with a clear focus on quality, soundness and long term progress.</p>
      <span class="btn-gold btn-small">READ MORE</span>
    </div>
    <div class="welcome-photo" role="img" aria-label="Bay horse rearing with a bridle, set against white"></div>
  </section>

  <section class="services">
    <h2 class="section-title">Our Services and Facilities</h2>
    <div class="dots">&bull;&bull;&bull;</div>
    <p class="services-text">Lorem Ipsum is simply dummy text of the printing and typesetting industry.</p>
  </section>
</div>
</body>
</html>
```